Amber Hollow Productions

I need a business card design for a new freelance film production company using or incorporating the logo:
I want the card to be creative, minimal, yet professional. Feel free to use a variety of different shapes and sizes/ textures for the card.

Industry/Entity Type

Film Production

```html
<!DOCTYPE html>
<html lang="en">
<head>
<meta charset="utf-8">
<title>Amber Hollow Productions – Business Card</title>
<link href="https://fonts.googleapis.com/css2?family=Lato:wght@400;700&display=swap" rel="stylesheet">
<style>
  :root {
    --brand-blue: #1354a8;
    --paper: #ffffff;
    --backdrop: #2a2a2a;
    --ink-light: #ffffff;
  }
  * { margin: 0; padding: 0; box-sizing: border-box; }
  html, body { width: 1200px; height: 900px; overflow: hidden; }
  body {
    background: var(--backdrop);
    font-family: "Lato", sans-serif;
    position: relative;
  }
  .card { position: absolute; width: 298px; }
  .card--front { left: 257px; top: 185px; height: 517px; }
  .card--back { left: 676px; top: 183px; height: 519px; width: 297px; }

  .skyline {
    position: absolute; left: 0; top: 0; width: 100%; height: 100px;
    background: linear-gradient(180deg, rgba(19,84,168,0.75), var(--brand-blue));
    clip-path: polygon(4% 45%, 12% 45%, 12% 25%, 22% 25%, 22% 8%, 30% 8%, 30% 0, 36% 0, 36% 8%, 46% 8%, 46% 22%, 56% 22%, 56% 30%, 66% 30%, 66% 18%, 76% 18%, 76% 40%, 86% 40%, 86% 55%, 100% 55%, 100% 100%, 0 100%, 0 60%);
  }
  .card-body {
    position: absolute; left: 0; right: 0; bottom: 0;
    border-radius: 0 0 8px 8px; overflow: hidden;
  }
  .card--front .card-body { top: 98px; background: var(--paper); }
  .card--front .top-band { height: 37px; background: var(--brand-blue); }
  .card--back .card-body { top: 96px; background: var(--brand-blue); }

  .logo-mark { position: absolute; }
  .card--front .logo-mark { left: 116px; top: 140px; width: 64px; height: 64px; background: var(--brand-blue); }
  .card--back .logo-mark { left: 70px; top: 228px; width: 92px; height: 92px; background: var(--ink-light); }

  .wordmark { position: absolute; color: var(--brand-blue); font-weight: 400; }
  .wordmark .name { display: block; line-height: 1; white-space: nowrap; }
  .wordmark .sub { display: block; letter-spacing: 0.42em; white-space: nowrap; }
  .card--front .wordmark { left: 6px; top: 214px; }
  .card--front .wordmark .name { font-size: 34px; }
  .card--front .wordmark .sub { font-size: 14px; margin-top: 12px; padding-left: 2px; }

  .person { position: absolute; left: 40px; top: 427px; color: var(--brand-blue); }
  .person .full-name { font-size: 19px; }
  .person .role { font-size: 11px; margin-top: 2px; }

  .card--back .wordmark { left: 54px; top: 331px; color: var(--ink-light); }
  .card--back .wordmark .name { font-size: 21px; }
  .card--back .wordmark .sub { font-size: 8px; margin-top: 4px; padding-left: 2px; }
  .divider { position: absolute; left: 54px; right: 0; top: 379px; height: 2px; background: var(--ink-light); }

  .contact { position: absolute; left: 56px; top: 390px; list-style: none; color: var(--ink-light); font-size: 11px; line-height: 15px; }
  .contact li { display: flex; align-items: flex-start; gap: 7px; }
  .contact svg { width: 10px; height: 10px; margin-top: 2px; flex: none; }
</style>
</head>
<body>
  <article class="card card--front">
    <div class="skyline" role="img" aria-label="City skyline die-cut silhouette"></div>
    <div class="card-body"><div class="top-band"></div></div>
    <div class="logo-mark" aria-hidden="true"></div>
    <div class="wordmark">
      <span class="name">AMBER HOLLOW</span>
      <span class="sub">PRODUCTIONS</span>
    </div>
    <div class="person">
      <p class="full-name">Mara Ellison</p>
      <p class="role">CEO, Founder</p>
    </div>
  </article>

  <article class="card card--back">
    <div class="skyline" role="img" aria-label="City skyline die-cut silhouette"></div>
    <div class="card-body"></div>
    <div class="logo-mark" aria-hidden="true"></div>
    <div class="wordmark">
      <span class="name">AMBER HOLLOW</span>
      <span class="sub">PRODUCTIONS</span>
    </div>
    <div class="divider"></div>
    <ul class="contact">
      <li><svg viewBox="0 0 10 10" fill="none" stroke="#fff" stroke-width="1.2"><path d="M5 9.5C2.5 6.5 2 5 2 4a3 3 0 0 1 6 0c0 1-.5 2.5-3 5.5z"/><circle cx="5" cy="4" r="1"/></svg><span>214 Larkspur Lane, CN2 | Rm. 45<br>Fairview | NY 10099</span></li>
      <li><svg viewBox="0 0 10 10" fill="none" stroke="#fff" stroke-width="1.2"><rect x="1" y="2.5" width="8" height="5.5"/><path d="M1 2.5l4 3 4-3"/></svg><span>info@amberhollowproductions.com</span></li>
      <li><svg viewBox="0 0 10 10" fill="none" stroke="#fff" stroke-width="1.1"><circle cx="5" cy="5" r="4"/><path d="M1 5h8M5 1c-2 2.5-2 5.5 0 8M5 1c2 2.5 2 5.5 0 8"/></svg><span>amberhollowproductions.com</span></li>
      <li><svg viewBox="0 0 10 10" fill="none" stroke="#fff" stroke-width="1.2"><circle cx="5" cy="5" r="4"/><path d="M3.5 3c0 2 1.5 3.5 3.5 3.5"/></svg><span>00198765432</span></li>
      <li><svg viewBox="0 0 10 10" fill="none" stroke="#fff" stroke-width="1.2"><rect x="1" y="4" width="8" height="4.5"/><rect x="3" y="1.5" width="4" height="2.5"/></svg><span>009-8765</span></li>
    </ul>
  </article>
</body>
</html>
```